Birch Lane Electical winter special

I need an ad for a print magazine for my electrical contracting business.
It must have my logo and business name as the main back ground with a banner over the top stating 'winter solar special 10% off'
it must have my licence number in the botomm right corner lic.528194K
It must have my name Derek Malloway ph 0491823576
Also I would like it to say somewher 'Call now for your free solar assessment'
I would like it on a sharp black bagground like my business card attached and flyer attached
This will be a in a landscape design not potrait
Target Market(s)
Print ad and banner advertising
Industry/Entity Type
Solar Energy
Colors
Designer to choose colors to be used in the design.
Requirements
Must have
- my licence number on bottom right corner
- lic.528194K

```html
<!DOCTYPE html>
<html lang="en">
<head>
<meta charset="utf-8">
<title>Birch Lane Electrical – Winter Solar Special</title>
<link rel="stylesheet" href="https://fonts.googleapis.com/css2?family=Oswald:wght@600&family=Open+Sans:ital,wght@0,400;0,600;0,700;1,600;1,700&display=swap">
<style>
  :root {
    --frame: #a9aaab;
    --card-top: #111111;
    --card-bottom: #000000;
    --brand-blue: #3f8fe0;
    --accent-blue: #4aa3ef;
    --badge-blue: #1d50a8;
    --text-light: #ececec;
    --text-grey: #b5b5b5;
    --band: #262626;
    --white: #ffffff;
  }
  * { box-sizing: border-box; margin: 0; padding: 0; }
  html, body { width: 1200px; height: 646px; overflow: hidden; }
  body { background: var(--frame); position: relative; font-family: "Open Sans", Arial, sans-serif; }

  .ad {
    position: absolute; left: 37px; top: 41px; width: 1126px; height: 563px;
    background: linear-gradient(180deg, var(--card-top), var(--card-bottom));
  }
  .brand {
    position: absolute; left: 32px; top: 62px; display: flex; align-items: center; gap: 12px;
    font-weight: 700; font-size: 30px; line-height: 1.05; color: var(--brand-blue); letter-spacing: 1px;
  }
  .brand-dot { width: 34px; height: 34px; border-radius: 50%; background: var(--brand-blue); flex: none; }

  .badge {
    position: absolute; left: 364px; top: 32px; width: 152px; height: 152px; border-radius: 50%;
    background: var(--badge-blue); color: var(--white); text-align: center;
    box-shadow: 0 3px 8px rgba(0,0,0,.6);
    z-index: 1;
  }
  .badge::before {
    content: ""; position: absolute; inset: 7px; border-radius: 50%;
    border: 1.5px dashed rgba(255,255,255,.8);
  }
  .badge-line { display: block; font-weight: 600; font-size: 17px; line-height: 19px; }
  .badge-line:first-child { margin-top: 28px; }
  .badge-offer { display: block; font-weight: 700; font-size: 40px; line-height: 44px; letter-spacing: -1px; }
  .badge-offer small { font-size: 26px; }

  .hero-art {
    position: absolute; left: 448px; top: 78px; width: 656px; height: 296px;
    background: linear-gradient(160deg, #2c4a6e 0%, #c9d6e2 45%, #5a5a5a 100%);
  }

  .headline {
    position: absolute; left: 30px; top: 213px;
    font-family: "Oswald", "Arial Narrow", sans-serif; font-weight: 600; font-size: 46px;
    color: var(--brand-blue); letter-spacing: 0;
  }
  .subline {
    position: absolute; left: 31px; top: 298px;
    font-size: 22px; line-height: 35px; color: var(--text-light);
    letter-spacing: .5px;
  }

  .services {
    position: absolute; left: 0; top: 396px; width: 100%; height: 64px; background: var(--band);
    text-align: center; font-size: 20.5px; line-height: 27px; color: var(--text-light); padding-top: 4px;
    letter-spacing: .3px;
  }
  .cta {
    position: absolute; left: 0; top: 470px; width: 100%; text-align: center;
    font-weight: 600; font-size: 23px; color: var(--accent-blue);
  }
  .contact {
    position: absolute; left: 0; top: 503px; width: 100%; text-align: center;
    font-style: italic; font-weight: 700; font-size: 27px; color: var(--text-light); letter-spacing: .8px;
  }
  .licence {
    position: absolute; right: 16px; bottom: 4px;
    font-style: italic; font-weight: 600; font-size: 13px; color: var(--text-grey);
  }
</style>
</head>
<body>
  <main class="ad">
    <div class="brand">
      <span class="brand-dot"></span>
      <span>BIRCH LANE<br>ELECTRICAL</span>
    </div>

    <div class="hero-art" role="img" aria-label="Illustration of solar panels, a yellow hard hat, a model house with trees and a calculator on rolled-out building plans"></div>

    <div class="badge">
      <span class="badge-line">winter solar</span>
      <span class="badge-line">special</span>
      <span class="badge-offer">10%<small>off</small></span>
    </div>

    <h1 class="headline">GO SOLAR ! GO ON...</h1>
    <p class="subline">Get Started Today &amp; Start Saving<br>Thousands on Electricity.</p>

    <section class="services">
      Specialising In: • Solar Design and Installation • All your domestic and commercial electrical needs<br>
      • Outstanding customer service • Competitive rates
    </section>

    <p class="cta">Call now for your free solar assessment’</p>
    <p class="contact">Derek Malloway | info@birchlaneelectrical.com.au | &nbsp;Ph. 0491 823 576</p>

    <p class="licence">Lic. 528194K</p>
  </main>
</body>
</html>
```